Business cards for law firm with global theme

I'd like business cards with contact info for two offices. They should include the colors and font of the new logo design, which is a stylized globe with an "F" in it. The feel should be very modern and professional.

```html
<!DOCTYPE html>
<html lang="en">
<head>
<meta charset="utf-8">
<title>Marvessa Law – Business Cards</title>
<link href="https://fonts.googleapis.com/css2?family=Lexend:wght@400;500;600&display=swap" rel="stylesheet">
<style>
  :root {
    --stage: #282828;
    --navy: #053e72;
    --sky: #00a3e4;
    --mid: #0b5a9c;
    --ink: #262626;
    --paper: #ffffff;
  }
  * { box-sizing: border-box; margin: 0; padding: 0; }
  html, body { width: 1075px; height: 1200px; overflow: hidden; }
  body {
    background: var(--stage);
    font-family: "Lexend", Arial, sans-serif;
    position: relative;
  }
  .card {
    position: absolute;
    width: 663px;
    height: 395px;
    box-shadow: 3px 3px 4px rgba(0,0,0,0.7);
    overflow: hidden;
  }
  /* Front */
  .card-front { left: 206px; top: 187px; background: var(--paper); }
  .band-dark { position: absolute; left: 0; top: 0; width: 470px; height: 105px; background: var(--navy); }
  .band-light { position: absolute; left: 470px; top: 0; width: 193px; height: 105px; background: var(--sky); }
  .brand-mark {
    position: absolute; left: 372px; top: 8px; width: 212px; height: 212px;
    border-radius: 50%; background: var(--mid); border: 9px solid var(--paper);
  }
  .front-brand {
    position: absolute; left: 30px; top: 24px;
    color: var(--paper); font-weight: 500; font-size: 38px; line-height: 1;
    letter-spacing: 0.5px;
  }
  .person { position: absolute; left: 26px; top: 186px; }
  .person-name { color: var(--navy); font-weight: 600; font-size: 23px; letter-spacing: 0.8px; line-height: 1.05; }
  .person-title { color: var(--sky); font-weight: 500; font-size: 19px; line-height: 1.1; }
  .office { position: absolute; top: 248px; }
  .office-left { left: 28px; }
  .office-right { right: 36px; text-align: right; top: 245px; }
  .office-heading { color: var(--navy); font-weight: 600; font-size: 20px; letter-spacing: 1px; margin-bottom: 4px; }
  .contact { color: var(--ink); font-weight: 500; display: flex; align-items: flex-start; gap: 6px; }
  .office-right .contact { justify-content: flex-end; }
  .contact-phone { font-size: 21px; letter-spacing: 0.5px; }
  .contact-email { font-size: 18px; letter-spacing: 0.5px; margin-top: 2px; }
  .contact-address { font-size: 19px; line-height: 1.3; margin-top: 4px; letter-spacing: 0.3px; }
  .icon { flex: none; width: 18px; height: 18px; fill: var(--sky); margin-top: 4px; }
  /* Back */
  .card-back {
    left: 203px; top: 637px;
    background: linear-gradient(35deg, #023a70 0%, #05569a 45%, #0088cc 78%, #00a3e4 100%);
    text-align: center; color: var(--paper);
  }
  .back-mark {
    position: absolute; left: 269px; top: 80px; width: 130px; height: 130px;
    border-radius: 50%; background: var(--paper);
  }
  .back-brand {
    position: absolute; left: 0; right: 0; top: 228px;
    font-weight: 500; line-height: 1; color: var(--paper);
  }
  .back-brand .brand-main { display: block; font-size: 56px; letter-spacing: 1px; }
  .back-brand .brand-sub { display: block; font-size: 38px; margin-top: 2px; }
  .back-url { position: absolute; left: 0; right: 0; top: 346px; font-size: 18px; font-weight: 500; letter-spacing: 0.5px; }
</style>
</head>
<body>
  <section class="card card-front" aria-label="Business card front">
    <div class="band-dark"></div>
    <div class="band-light"></div>
    <div class="brand-mark" aria-hidden="true"></div>
    <div class="front-brand">MARVESSA LAW</div>

    <div class="person">
      <p class="person-name">DANIEL HARTLEY</p>
      <p class="person-title">Managing Director</p>
    </div>

    <div class="office office-left">
      <p class="office-heading">MARVESSA OFFICE</p>
      <p class="contact contact-phone">
        <svg class="icon" viewBox="0 0 24 24"><path d="M6.6 10.8a15.1 15.1 0 0 0 6.6 6.6l2.2-2.2a1 1 0 0 1 1-.25 11.4 11.4 0 0 0 3.6.57 1 1 0 0 1 1 1V20a1 1 0 0 1-1 1A17 17 0 0 1 3 4a1 1 0 0 1 1-1h3.5a1 1 0 0 1 1 1c0 1.25.2 2.45.57 3.57a1 1 0 0 1-.25 1z"/></svg>
        044-555 018 270</p>
      <p class="contact contact-email">
        <svg class="icon" viewBox="0 0 24 24"><path d="M2 5h20v14H2z M2 5l10 8 10-8" fill="var(--sky)"/><path d="M2 5l10 8 10-8" fill="none" stroke="#fff" stroke-width="1.5"/></svg>
        hello@marvessa.com</p>
      <p class="contact contact-address">
        <svg class="icon" viewBox="0 0 24 24"><path d="M12 2a7 7 0 0 0-7 7c0 5 7 13 7 13s7-8 7-13a7 7 0 0 0-7-7zm0 9.5A2.5 2.5 0 1 1 12 6.5a2.5 2.5 0 0 1 0 5z"/></svg>
        <span>Address line goes here<br>45452,Country Name</span></p>
    </div>

    <div class="office office-right">
      <p class="office-heading">MARVESSA OFFICE</p>
      <p class="contact contact-phone">044-555 018 270
        <svg class="icon" viewBox="0 0 24 24"><path d="M6.6 10.8a15.1 15.1 0 0 0 6.6 6.6l2.2-2.2a1 1 0 0 1 1-.25 11.4 11.4 0 0 0 3.6.57 1 1 0 0 1 1 1V20a1 1 0 0 1-1 1A17 17 0 0 1 3 4a1 1 0 0 1 1-1h3.5a1 1 0 0 1 1 1c0 1.25.2 2.45.57 3.57a1 1 0 0 1-.25 1z"/></svg></p>
      <p class="contact contact-email">hello@marvessa.com
        <svg class="icon" viewBox="0 0 24 24"><path d="M2 5h20v14H2z" fill="var(--sky)"/><path d="M2 5l10 8 10-8" fill="none" stroke="#fff" stroke-width="1.5"/></svg></p>
      <p class="contact contact-address"><span>Address line goes here<br>45452,Country Name</span>
        <svg class="icon" viewBox="0 0 24 24"><path d="M12 2a7 7 0 0 0-7 7c0 5 7 13 7 13s7-8 7-13a7 7 0 0 0-7-7zm0 9.5A2.5 2.5 0 1 1 12 6.5a2.5 2.5 0 0 1 0 5z"/></svg></p>
    </div>
  </section>

  <section class="card card-back" aria-label="Business card back">
    <div class="back-mark" aria-hidden="true"></div>
    <p class="back-brand"><span class="brand-main">MARVESSA</span><span class="brand-sub">LAW</span></p>
    <p class="back-url">www.marvessalaw.com</p>
  </section>
</body>
</html>
```